Baked goods front of bag sticker

Toffelwick Brownies,
2 Go size (clear plastic bag of handful of ¼” square bites)
There will also be larger sizes and custom options(corporate/events) using the same image.
Deliverables Needed:
Need sticker with “Toffelwick Brownies” for front of bag, approximate 2” circle or rectangle/square.
Packaging front sticker design should be sizable for other media, ie website, future packaging, logo.
Flavor should be indicated on second sticker that integrates well.
Back sticker is already complete and includes ingredients, company name, health dept permit, and other legal necessities. Font will be changed to integrate with front.
Flavors:
1. Porchlight Caramel Brownie
2. Butterscotch Meadow Brownie
3. Zippity Chocolate
4. Tender Gluten Free (not so gooey but great)
Primary Audiences:
Anyone who wants a sweet treat to enjoy, and maybe share, on the go. Audience wants a fresh treat with real ingredients they know and love (real butter, Pure vanilla, Fresh eggs)
Audience wants something from a baker not a machine.
Sold at checkout in stores that don’t have baked goods, higher end convenience stores, specialty stores, small gourmet stores, theaters, toy stores, sports arenas, etc.
Will be sampled at events (festivals, movie screenings, races)
Tone and Image:
Fresh, Fun and frank with real ingredients you know
Because it is little and is home-baked, it should be perceived as a little treat without the guilt.
Messages:
Fresh, natural, little treat on the run.
Dear Designers,

```html
<!DOCTYPE html>
<html lang="en">
<head>
<meta charset="utf-8">
<title>Toffelwick Brownies – Flavour Stickers</title>
<link rel="stylesheet" href="https://fonts.googleapis.com/css2?family=Alex+Brush&family=Open+Sans:wght@400&family=Oswald:wght@500&display=swap">
<style>
  :root {
    --page: #ffffff;
    --teal: #14b8b6;
    --teal-deep: #0fa9a8;
    --cocoa: #7a3a1a;
    --brown-text: #8a4a22;
    --gold-light: #fbeec0;
    --gold-mid: #e2c47d;
    --gold-deep: #b98d45;
    --plaque-text: #f6dca0;
    --swirl: rgba(140, 95, 60, 0.35);
  }
  * { box-sizing: border-box; margin: 0; padding: 0; }
  html, body { width: 1200px; height: 1027px; overflow: hidden; background: var(--page); }
  .sheet { position: relative; width: 1200px; height: 1027px; }

  .sticker {
    position: absolute;
    width: 420px;
    height: 440px;
    padding: 18px;
    background: linear-gradient(135deg, var(--gold-deep) 0%, var(--gold-light) 22%, var(--gold-mid) 45%, var(--gold-light) 70%, var(--gold-deep) 100%);
  }
  .sticker--gluten-free  { left: 106px; top: 46px; }
  .sticker--chocolate    { left: 645px; top: 46px; }
  .sticker--caramel      { left: 106px; top: 531px; }
  .sticker--butterscotch { left: 645px; top: 531px; }

  .field {
    position: relative;
    width: 100%;
    height: 100%;
    background: radial-gradient(circle at 50% 45%, var(--teal) 0%, var(--teal-deep) 100%);
    overflow: hidden;
  }

  .flourish {
    position: absolute;
    width: 110px;
    height: 100px;
    background: radial-gradient(ellipse at center, var(--swirl) 0%, rgba(140,95,60,0.12) 55%, rgba(140,95,60,0) 75%);
  }
  .flourish--top { right: -10px; top: -8px; }
  .flourish--bottom { left: -12px; bottom: -6px; }

  .brand {
    position: absolute;
    left: 0; right: 0;
    top: 50px;
    text-align: center;
    font-family: "Alex Brush", cursive;
    font-size: 80px;
    line-height: 1.1;
    font-variant-ligatures: none;
    white-space: nowrap;
    color: var(--brown-text);
  }
  .brand--gold {
    background: linear-gradient(180deg, var(--gold-light) 0%, var(--gold-mid) 55%, var(--gold-deep) 100%);
    -webkit-background-clip: text;
    background-clip: text;
    color: transparent;
  }
  .brand-sub {
    position: absolute;
    right: 34px;
    top: 142px;
    font-family: "Open Sans", sans-serif;
    font-size: 27px;
    line-height: 1;
    color: var(--brown-text);
  }

  .brownie-photo {
    position: absolute;
    left: 162px;
    top: 196px;
    width: 60px;
    height: 60px;
    border-radius: 50%;
    background: radial-gradient(circle at 40% 35%, #8a5a3a 0%, #4a2a18 60%, #2b170d 100%);
    z-index: 2;
  }

  .plaque {
    position: absolute;
    left: 64px;
    top: 240px;
    width: 256px;
    height: 106px;
  }
  .plaque svg { position: absolute; inset: 0; width: 100%; height: 100%; }
  .plaque-name {
    position: absolute;
    inset: 16px 12px 10px;
    display: flex;
    align-items: center;
    justify-content: center;
    text-align: center;
    white-space: nowrap;
    font-family: "Oswald", sans-serif;
    font-weight: 500;
    font-size: 28px;
    line-height: 1.2;
    color: var(--plaque-text);
  }
  .plaque-name--long { font-size: 23px; }
</style>
</head>
<body>
<main class="sheet">

  <svg width="0" height="0" style="position:absolute" aria-hidden="true">
    <defs>
      <path id="plaque-shape" d="M40 18 Q56 18 62 10 Q70 2 86 6 Q104 12 124 4 Q144 12 162 6 Q178 2 186 10 Q192 18 208 18 Q232 20 234 40 Q246 52 234 64 Q232 84 208 86 Q192 86 186 94 Q178 102 162 98 Q144 92 124 100 Q104 92 86 98 Q70 102 62 94 Q56 86 40 86 Q16 84 14 64 Q2 52 14 40 Q16 20 40 18 Z"/>
    </defs>
  </svg>

  <section class="sticker sticker--gluten-free">
    <div class="field">
      <div class="flourish flourish--top" role="img" aria-label="Decorative scroll flourish"></div>
      <div class="flourish flourish--bottom" role="img" aria-label="Decorative scroll flourish"></div>
      <p class="brand">Toffelwick</p>
      <p class="brand-sub">Brownies</p>
      <div class="brownie-photo" role="img" aria-label="Photo of a gluten free brownie bite"></div>
      <div class="plaque">
        <svg viewBox="0 0 248 104" preserveAspectRatio="none" aria-hidden="true"><use href="#plaque-shape" fill="var(--cocoa)" stroke="var(--gold-mid)" stroke-width="2.5"/></svg>
        <p class="plaque-name">Tender Gluten<br>Free</p>
      </div>
    </div>
  </section>

  <section class="sticker sticker--chocolate">
    <div class="field">
      <div class="flourish flourish--top" role="img" aria-label="Decorative scroll flourish"></div>
      <div class="flourish flourish--bottom" role="img" aria-label="Decorative scroll flourish"></div>
      <p class="brand brand--gold">Toffelwick</p>
      <p class="brand-sub">Brownies</p>
      <div class="brownie-photo" role="img" aria-label="Photo of a chocolate brownie bite"></div>
      <div class="plaque">
        <svg viewBox="0 0 248 104" preserveAspectRatio="none" aria-hidden="true"><use href="#plaque-shape" fill="var(--cocoa)" stroke="var(--gold-mid)" stroke-width="2.5"/></svg>
        <p class="plaque-name">Zippity<br>Chocolate</p>
      </div>
    </div>
  </section>

  <section class="sticker sticker--caramel">
    <div class="field">
      <div class="flourish flourish--top" role="img" aria-label="Decorative scroll flourish"></div>
      <div class="flourish flourish--bottom" role="img" aria-label="Decorative scroll flourish"></div>
      <p class="brand brand--gold">Toffelwick</p>
      <p class="brand-sub">Brownies</p>
      <div class="brownie-photo" role="img" aria-label="Photo of a caramel brownie bite"></div>
      <div class="plaque">
        <svg viewBox="0 0 248 104" preserveAspectRatio="none" aria-hidden="true"><use href="#plaque-shape" fill="var(--cocoa)" stroke="var(--gold-mid)" stroke-width="2.5"/></svg>
        <p class="plaque-name plaque-name--long">Porchlight Caramel<br>Brownie</p>
      </div>
    </div>
  </section>

  <section class="sticker sticker--butterscotch">
    <div class="field">
      <div class="flourish flourish--top" role="img" aria-label="Decorative scroll flourish"></div>
      <div class="flourish flourish--bottom" role="img" aria-label="Decorative scroll flourish"></div>
      <p class="brand">Toffelwick</p>
      <p class="brand-sub">Brownies</p>
      <div class="brownie-photo" role="img" aria-label="Photo of a butterscotch brownie bite"></div>
      <div class="plaque">
        <svg viewBox="0 0 248 104" preserveAspectRatio="none" aria-hidden="true"><use href="#plaque-shape" fill="var(--cocoa)" stroke="var(--gold-mid)" stroke-width="2.5"/></svg>
        <p class="plaque-name plaque-name--long">Butterscotch Meadow<br>Brownie</p>
      </div>
    </div>
  </section>

</main>
</body>
</html>
```